Prairie Reading Alliance - Minds Unbound Website

We need a website designed for a PR + Marketing Campaign (Minds Unbound: Our Daily Craft) for the Prairie Reading Alliance (PRA), the largest statewide library association in the country.

The final design should communicate an empowerment to libraries, its innovative practices, and how they are helping and improving the lives of all communities (of all ages, backgrounds, experiences).

The look should be bold, captivating; meanwhile also simple, clean, easy-to-navigate.

LAYOUT (five pages total):
Page 1: Home – Intro
Animated logo transitioning into simple landing page.
Must feature #shelvesinmotion and eventually featuring video.

Page 2: About the Campaign
Graphics/photos optional, text below:
Broad Objectives and Goals
Minds Unbound: Our Daily Craft seeks to broaden the awareness of library services to the public and provide resources to librarians working in the state in order to promote libraries as vital, technology-centered institutions in the community.
The campaign provides a platform for the sharing of ideas and resources that strengthen the image of the library profession and the services provided by libraries in Texas.
Related goals include: providing librarians with the tools necessary to influence key supporters, shifting the perspectives of libraries as a center for books to a center for emerging technology and the cultivation of ideas, and spreading the message of the campaign through both traditional and social media outlets.
Librarians and information professionals are encouraged to actively participate in the campaign through social media outlets, using the hashtag #shelvesinmotion, and by contributing content in the Ideas Shared portion of the campaign website.

Page 3: Toolkit – downloadable items
Downloadable Campaign Materials for library professionals
Buttons leading to subpages or one large page covering the topics below

Page 4: Ideas Shared: What We Do: Interactive element page
Toolkit
Here are the tools and downloadable materials for #shelvesinmotion everywhere. Use these campaign designs to showcase the innovation happening in your library! Check back as we continue to update this page with new content.
Logos
Campaign logos in various formats for use on your own customized designs.
Print Materials
Flyers, bookmarks, posters and more!
Web & Interactive
Graphics for social media and the Web.
Coming soon: #shelvesinmotion campaign video!
PR & Marketing
Sample press releases, emails, and customizable content for a variety of library types: school, academic, public, and special.

Page 5: Contact Us Page
Can either be a sub-section of the About Us page, or a stand-alone link.
Standard submission form with the ability to upload documents for the Ideas Shared section.
Contact Us
Have a question or comment? Want to contribute a summary and photos or video of your innovative programs for the Ideas Shared section? Please get in touch!
NAME:
EMAIL:
PHONE:
ADDRESS: ?
MESSAGE:
ATTACHMENTS (upload)

MUST HAVE:
-Maintain the color-scheme of the logo (attached)
-The WEBSITE design must innovation and excitement. a contemporary design/layout that demonstrates vitality
-Somewhere on every page, we would like an interactive element for viewers, such as a stream from Chatterloop/Peepline with hashtags.
-Countdown to Campaign Launch
-Can we include animation? We are striving to create movement with the abstract icon in our log.

PLEASE AVOID:
-NO pastels, NO soft colors, nothing that might be considered feminine (pinks, etc); we do want to stear away from stereotypes (NO books, NO library buildings, NO reading conceptual designs) and standard icons (NO lightbulbs and NO lightning designs)

AUDIENCE/MARKET:
THE PUBLIC (also includes all kinds of librarians and their supporters: information, reference, school, public, special, law, academic, students, educators, administration, support staff, lay and advocates)

AUDIENCE/MARKET:

Requirements
Must have
• The final design should communicate an empowerment to libraries, its innovative practices, and how they are helping and improving the lives of all communities (of all ages, backgrounds, experiences).
• The look should be bold, captivating; meanwhile also simple, clean, easy-to-navigate.
• LAYOUT (five pages total):
• Page 1: Home – Intro
• Animated logo transitioning into simple landing page.
• Must feature #shelvesinmotion and eventually featuring video.
• Page 2: About the Campaign
• Graphics/photos optional, text below:
• Broad Objectives and Goals
• Minds Unbound: Our Daily Craft seeks to broaden the awareness of library services to the public and provide resources to librarians working in the state in order to promote libraries as vital, technology-centered institutions in the community.
• The campaign provides a platform for the sharing of ideas and resources that strengthen the image of the library profession and the services provided by libraries in Texas.
• Related goals include: providing librarians with the tools necessary to influence key supporters, shifting the perspectives of libraries as a center for books to a center for emerging technology and the cultivation of ideas, and spreading the message of the campaign through both traditional and social media outlets.
• Librarians and information professionals are encouraged to actively participate in the campaign through social media outlets, using the hashtag #shelvesinmotion, and by contributing content in the Ideas Shared portion of the campaign website.
• Page 3: Toolkit – downloadable items
• Downloadable Campaign Materials for library professionals
• Buttons leading to subpages or one large page covering the topics below
• Page 4: Ideas Shared: What We Do: Interactive element page
• Toolkit
• Here are the tools and downloadable materials for #shelvesinmotion everywhere. Use these campaign designs to showcase the innovation happening in your library! Check back as we continue to update this page with new content.
• Logos
• Campaign logos in various formats for use on your own customized designs.
• Print Materials
• Flyers, bookmarks, posters and more!
• Web & Interactive
• Graphics for social media and the Web.
• Coming soon: #shelvesinmotion campaign video!
• PR & Marketing
• Sample press releases, emails, and customizable content for a variety of library types: school, academic, public, and special.
• Page 5: Contact Us Page
• Can either be a sub-section of the About Us page, or a stand-alone link.
• Standard submission form with the ability to upload documents for the Ideas Shared section.
• Contact Us
• Have a question or comment? Want to contribute a summary and photos or video of your innovative programs for the Ideas Shared section? Please get in touch!
• NAME:
• EMAIL:
• PHONE:
• ADDRESS: ?
• MESSAGE:
• ATTACHMENTS (upload)
• MUST HAVE:
• -Maintain the color-scheme of the logo (attached)
• -The WEBSITE design must innovation and excitement. a contemporary design/layout that demonstrates vitality
• -Somewhere on every page, we would like an interactive element for viewers, such as a stream from Chatterloop/Peepline with hashtags.
• -Countdown to Campaign Launch
• -Can we include animation? We are striving to create movement with the abstract icon in our log.
Should not have
• PLEASE AVOID:
• -NO pastels, NO soft colors, nothing that might be considered feminine (pinks, etc); we do want to stear away from stereotypes (NO books, NO library buildings, NO reading conceptual designs) and standard icons (NO lightbulbs and NO lightning designs)

```html
<!DOCTYPE html>
<html lang="en">
<head>
<meta charset="utf-8">
<title>Minds Unbound: Our Daily Craft – Website Screens</title>
<link rel="stylesheet" href="https://fonts.googleapis.com/css2?family=Source+Sans+3:wght@300;400;600;700&display=swap">
<style>
  :root{
    --stage:#5ee6f7;
    --brand-blue:#3aa6dc;
    --brand-blue-soft:#7cc3e6;
    --brand-deep:#14506f;
    --paper:#ffffff;
    --mist:#ececec;
    --ink:#3a3a3a;
    --ink-soft:#7a7a7a;
    --line:#5bb6e0;
  }
  *{box-sizing:border-box;margin:0;padding:0}
  html,body{width:1200px;height:518px;overflow:hidden}
  body{background:var(--stage);font-family:"Source Sans 3",sans-serif;color:var(--ink);position:relative}

  .stage-title{position:absolute;top:66px;left:0;right:0;text-align:center;color:var(--paper);font-size:21px;font-weight:600;letter-spacing:.3px}

  .screen{position:absolute;top:130px;width:370px;height:340px;background:var(--paper);overflow:hidden;box-shadow:0 6px 18px rgba(0,60,80,.25)}
  .screen--toolkit{left:28px}
  .screen--home{left:415px}
  .screen--contact{left:802px}

  /* Toolkit screen */
  .toolkit-intro{height:88px;background:var(--mist);text-align:center;padding:22px 34px 0}
  .page-title{font-weight:400;font-size:13px;letter-spacing:.5px;color:var(--ink)}
  .intro-copy{margin-top:9px;font-size:5.4px;line-height:1.5;color:var(--ink-soft)}
  .toolkit-band{height:92px;background:var(--brand-blue);color:var(--paper);text-align:center;padding-top:24px;position:relative}
  .band-title{font-weight:400;font-size:11px}
  .band-copy{margin-top:12px;font-size:5.4px;opacity:.9}
  .band-pager{position:absolute;left:50%;bottom:7px;transform:translateX(-50%)}
  .tile-row{display:flex;height:160px}
  .tile{flex:1;display:flex;align-items:center;justify-content:center;text-align:center}
  .tile--a{background:linear-gradient(160deg,#ebe8e3,#c6c2bc)}
  .tile--b{background:var(--brand-blue-soft);color:var(--paper);font-size:11px;line-height:1.25}
  .tile--c{background:linear-gradient(160deg,#f2f2f0,#d4d4d0)}

  /* Home screen */
  .hero{position:absolute;inset:0;background:
    linear-gradient(90deg,rgba(20,80,111,.0) 0%,rgba(20,80,111,.35) 70%,rgba(255,255,255,.25) 100%),
    linear-gradient(180deg,#5d98b8 0%,#2c76a3 28%,#1d5f88 55%,#3b8dbb 78%,#dfe9ee 100%)}
  .home-nav{position:absolute;top:0;left:0;right:0;height:38px;display:flex;justify-content:center;align-items:flex-end;gap:14px;padding-bottom:7px;background:rgba(255,255,255,.2)}
  .home-nav a{font-size:6.5px;letter-spacing:.4px;color:var(--paper);text-decoration:none}
  .home-nav a.is-current{color:var(--brand-deep);font-weight:700;position:relative}
  .home-nav a.is-current::before{content:"";position:absolute;left:50%;top:-20px;width:1px;height:12px;background:var(--brand-deep)}
  .campaign-mark{position:absolute;left:0;right:0;top:108px;text-align:center;color:var(--paper)}
  .mark-square{display:inline-block;width:22px;height:22px;border:2px solid var(--paper);margin-bottom:7px}
  .mark-name{font-size:11px;font-weight:600;letter-spacing:1.4px;line-height:1.3}
  .countdown{position:absolute;left:0;right:0;top:196px;display:flex;justify-content:center;gap:6px}
  .countdown-unit{width:34px;padding:4px 0 3px;background:rgba(255,255,255,.16);border:1px solid rgba(255,255,255,.6);text-align:center;color:var(--paper)}
  .countdown-value{display:block;font-size:11px;font-weight:700;line-height:1}
  .countdown-label{display:block;margin-top:2px;font-size:4.6px;letter-spacing:.6px}
  .countdown-caption{position:absolute;left:0;right:0;top:184px;text-align:center;font-size:5.4px;letter-spacing:1px;color:var(--paper)}
  .slider-controls{position:absolute;left:50%;bottom:26px;transform:translateX(-50%)}

  /* Contact screen */
  .contact-topbar{height:16px;background:var(--brand-blue);color:var(--paper);display:flex;justify-content:space-between;align-items:center;padding:0 10px;font-size:5.2px}
  .social-links{display:flex;gap:6px}
  .contact-nav{height:36px;display:flex;justify-content:flex-end;align-items:flex-end;gap:10px;padding:0 18px 7px;background:var(--mist)}
  .contact-nav a{font-size:6px;color:var(--ink);text-decoration:none}
  .contact-nav a.is-current{color:var(--brand-blue);position:relative}
  .contact-nav a.is-current::before{content:"";position:absolute;left:50%;top:-16px;width:1px;height:10px;background:var(--brand-blue)}
  .contact-form{padding:20px 26px 0;text-align:center}
  .form-title{font-size:10px;font-weight:400}
  .form-copy{margin:6px auto 0;width:240px;font-size:4.8px;line-height:1.5;color:var(--ink-soft)}
  .field-row{display:flex;gap:14px;margin-top:18px}
  .field{flex:1;height:11px;border:1px solid var(--line);border-radius:2px;font-size:4.8px;color:#9ab;text-align:left;padding-left:4px;line-height:9px}
  .field--message{height:76px;margin-top:6px}
  .form-actions{display:flex;gap:6px;margin-top:7px}
  .btn{width:24px;height:9px;font-size:4.4px;line-height:9px;border:1px solid var(--line);color:var(--brand-blue);text-align:center}
  .btn--primary{background:var(--brand-blue);color:var(--paper)}
  .contact-footer{display:flex;justify-content:space-between;align-items:center;padding:24px 26px 0;font-size:5.2px;font-weight:600}
  .footer-item{display:flex;align-items:center;gap:6px}
</style>
</head>
<body>

  <h1 class="stage-title">MINDS UNBOUND - OUR DAILY CRAFT</h1>

  <section class="screen screen--toolkit" aria-label="Toolkit page">
    <header class="toolkit-intro">
      <h2 class="page-title">TOOLKIT</h2>
      <p class="intro-copy">Here are the tools and downloadable materials for #shelvesinmotion everywhere. Use these campaign designs to showcase the innovation happening in your library! Check back as we continue to update this page with new content.</p>
    </header>
    <div class="toolkit-band">
      <h3 class="band-title">LOGOS</h3>
      <p class="band-copy">Campaign logos in various formats for use on your own customized designs.</p>
      <svg class="band-pager" width="20" height="10" viewBox="0 0 20 10" aria-hidden="true">
        <path d="M7 1 3 5l4 4" fill="none" stroke="#ffffff" stroke-opacity=".5" stroke-width="1"/>
        <path d="M13 1l4 4-4 4" fill="none" stroke="#ffffff" stroke-width="1"/>
      </svg>
    </div>
    <div class="tile-row">
      <div class="tile tile--a" role="img" aria-label="Sample logo printed on textured paper"></div>
      <div class="tile tile--b">HOVER FOR<br>TITLE + LINK</div>
      <div class="tile tile--c" role="img" aria-label="Sample logo printed on white card"></div>
    </div>
  </section>

  <section class="screen screen--home" aria-label="Home page">
    <div class="hero" role="img" aria-label="Blurred background photo for the landing slider"></div>
    <nav class="home-nav">
      <a href="#" class="is-current">HOME</a>
      <a href="#">ABOUT</a>
      <a href="#">TOOLKIT</a>
      <a href="#">IDEAS SHARED</a>
      <a href="#">CONTACT</a>
    </nav>
    <div class="campaign-mark">
      <span class="mark-square" aria-hidden="true"></span>
      <p class="mark-name">MINDS UNBOUND<br>OUR DAILY CRAFT</p>
    </div>
    <p class="countdown-caption">CAMPAIGN LAUNCH IN</p>
    <div class="countdown" aria-label="Countdown to campaign launch">
      <div class="countdown-unit"><span class="countdown-value">12</span><span class="countdown-label">DAYS</span></div>
      <div class="countdown-unit"><span class="countdown-value">08</span><span class="countdown-label">HOURS</span></div>
      <div class="countdown-unit"><span class="countdown-value">45</span><span class="countdown-label">MINS</span></div>
      <div class="countdown-unit"><span class="countdown-value">30</span><span class="countdown-label">SECS</span></div>
    </div>
    <svg class="slider-controls" width="60" height="14" viewBox="0 0 60 14" aria-label="Slider controls">
      <g fill="none" stroke="#14506f" stroke-width="1.2">
        <path d="M3 1v12M12 1 5 7l7 6z"/>
        <rect x="23" y="1" width="12" height="12" fill="#ffffff" fill-opacity=".7"/>
        <path d="M57 1v12M48 1l7 6-7 6z"/>
      </g>
    </svg>
  </section>

  <section class="screen screen--contact" aria-label="Contact page">
    <div class="contact-topbar">
      <span>hello@mindsunbound.org</span>
      <span class="social-links"><span>Chatterloop</span><span>Peepline</span></span>
    </div>
    <nav class="contact-nav">
      <a href="#">HOME</a>
      <a href="#">ABOUT</a>
      <a href="#">TOOLKIT</a>
      <a href="#">IDEAS SHARED</a>
      <a href="#" class="is-current">CONTACT</a>
    </nav>
    <form class="contact-form">
      <h2 class="form-title">CONTACT FORM</h2>
      <p class="form-copy">Have a question or comment? Want to contribute a summary and photos or video of your innovative programs for the Ideas Shared section? Please get in touch!</p>
      <div class="field-row">
        <div class="field">Name</div>
        <div class="field">Email</div>
        <div class="field">Phone</div>
      </div>
      <div class="field field--message"></div>
      <div class="form-actions">
        <span class="btn btn--primary">SEND</span>
        <span class="btn">CLEAR</span>
      </div>
    </form>
    <footer class="contact-footer">
      <div class="footer-item"><span>MY TEXT<br>YOUR ADDRESS</span></div>
      <div class="footer-item">
        <svg width="12" height="9" viewBox="0 0 12 9" aria-hidden="true"><rect width="12" height="9" fill="#3aa6dc"/><path d="M0 0l6 5 6-5" fill="none" stroke="#ffffff" stroke-width="1"/></svg>
        <span>HELLO@MINDSUNBOUND.ORG</span>
      </div>
      <div class="footer-item">
        <svg width="10" height="12" viewBox="0 0 10 12" aria-hidden="true"><path d="M2 0h2l1 3-1.5 1.2a7 7 0 0 0 3 4L8 7l2 1v2.5C10 11 9 12 8 12 3.5 11.5 0 7 0 2 0 1 1 0 2 0z" fill="#3aa6dc"/></svg>
        <span>000 00 00 00<br>000 00 00 00</span>
      </div>
    </footer>
  </section>

</body>
</html>
```